Singapore celebrates National Day (Independence Day) every year.

There are parties or gatherings around the country and our group plans to host one.

This will be a generic poster that ideally can be recycled over the years so there shouldn't be any reference to 2013 or anything that will make it look outdated in the next 2-3 years.

The party will have both adults and kids and will have good food, games (not the kiddie ones) & prizes.

In a nutshell, it's about celebrating Singapore as a country, what's good about it (good food, clean & green city, safe & secure, modern, everything works, great shopping & entertainment, honest government, preferred city to do business, embraces all races).

Adults 25-40 years old

• Infographics format

Title should be Singapore National Day Party

Must have these elements:
- Singapore flag
- Fireworks
- Celebration - food, drinks
- People - multi-racial in harmony (Chinese, Malay, Indian, others)

Colors - predominantly red and white

Icons - Halvorn Crest Suites, Veltrana, Quorbel, Dunmoor Spindle, Singapore Flag

• One of these tag lines:

"Keep Dancing, Tollvane!"

"Tollvane: Bright Days"

"Many Voices, Shared Path, Tollvane Forever"
• Real photos of Singapore, should only be illustration

Should not look like it's a children's party

```html
<!DOCTYPE html>
<html lang="en">
<head>
<meta charset="utf-8">
<title>Singapore National Day Party</title>
<link rel="stylesheet" href="https://fonts.googleapis.com/css2?family=Anton&family=Archivo+Black&family=Oswald:wght@600&display=swap">
<style>
  :root {
    --red: #d9141f;
    --red-deep: #a50a12;
    --red-soft: #ec3b44;
    --white: #ffffff;
    --paper: #f1f1f1;
    --band-edge: #bdbdbd;
    --slate: #3d3d3f;
    --slate-dark: #262628;
    --shadow: rgba(0, 0, 0, 0.3);
    --ring: #cfc6a0;
  }
  * { margin: 0; padding: 0; box-sizing: border-box; }
  html, body { width: 800px; height: 1200px; overflow: hidden; background: var(--white); }
  .poster {
    position: relative;
    width: 800px;
    height: 1200px;
    overflow: hidden;
    background: radial-gradient(ellipse at 40% 55%, var(--red-soft), var(--red) 55%, var(--red-deep));
  }
  .poster-art { position: absolute; inset: 0; width: 800px; height: 1200px; }
  .title-text {
    font-family: "Anton", "Oswald", sans-serif;
    font-size: 44px;
    fill: var(--red);
  }
  .motto { position: absolute; left: 0; top: 0; width: 800px; height: 1200px; }
  .motto-tab {
    position: absolute;
    display: flex;
    align-items: stretch;
    transform: rotate(-5deg);
    transform-origin: left center;
    box-shadow: 6px 10px 14px var(--shadow);
  }
  .motto-badge {
    width: 118px;
    flex: none;
    display: flex;
    align-items: center;
    justify-content: center;
    background: linear-gradient(180deg, var(--slate), var(--slate-dark));
  }
  .motto-ring {
    width: 72px;
    height: 72px;
    border-radius: 50%;
    border: 3px solid var(--ring);
    display: flex;
    align-items: center;
    justify-content: center;
    font-family: "Oswald", sans-serif;
    font-weight: 600;
    font-size: 14px;
    letter-spacing: 0.5px;
    color: var(--ring);
    text-transform: uppercase;
  }
  .motto-word {
    flex: 1;
    display: flex;
    align-items: center;
    padding-left: 22px;
    background: linear-gradient(180deg, var(--red-soft), var(--red) 60%, var(--red-deep));
    font-family: "Archivo Black", sans-serif;
    font-size: 46px;
    color: var(--white);
    text-shadow: 2px 3px 3px var(--shadow);
  }
  .motto-tab--first  { left: 300px; top: 470px; width: 400px; height: 100px; }
  .motto-tab--second { left: 220px; top: 660px; width: 480px; height: 100px; }
  .motto-tab--third  { left: 140px; top: 850px; width: 520px; height: 104px; }
</style>
</head>
<body>
<main class="poster">
  <svg class="poster-art" viewBox="0 0 800 1200" xmlns="http://www.w3.org/2000/svg">
    <defs>
      <linearGradient id="flag-fill" x1="0" y1="0" x2="0.15" y2="1">
        <stop offset="0" stop-color="#e0141e"/>
        <stop offset="0.4" stop-color="#e0141e"/>
        <stop offset="0.5" stop-color="#f7f7f7"/>
        <stop offset="1" stop-color="#d8d8d8"/>
      </linearGradient>
      <radialGradient id="burst-fill" cx="0.5" cy="0.5" r="0.5">
        <stop offset="0" stop-color="#ffffff" stop-opacity="0.85"/>
        <stop offset="0.4" stop-color="#f7a5a9" stop-opacity="0.55"/>
        <stop offset="1" stop-color="#d9141f" stop-opacity="0"/>
      </radialGradient>
      <linearGradient id="crowd-fill" x1="0" y1="0" x2="0" y2="1">
        <stop offset="0" stop-color="#f6b9bc" stop-opacity="0"/>
        <stop offset="0.3" stop-color="#f6c3c5" stop-opacity="0.85"/>
        <stop offset="1" stop-color="#ffffff"/>
      </linearGradient>
    </defs>

    <g class="fireworks" role="img" aria-label="White fireworks bursting across the red sky">
      <circle cx="130" cy="300" r="150" fill="url(#burst-fill)"/>
      <circle cx="90" cy="580" r="160" fill="url(#burst-fill)"/>
      <circle cx="330" cy="560" r="100" fill="url(#burst-fill)"/>
      <circle cx="700" cy="700" r="110" fill="url(#burst-fill)"/>
      <circle cx="420" cy="330" r="70" fill="url(#burst-fill)"/>
    </g>

    <polygon class="flag" points="81,0 800,0 800,444" fill="url(#flag-fill)"
             role="img" aria-label="Waving national flag, red over white with crescent and five stars"/>

    <polygon class="title-band" points="0,-50 800,444 800,554 0,60" fill="var(--white)"/>
    <polygon class="title-band-edge" points="0,60 800,554 800,570 0,76" fill="var(--band-edge)"/>

    <text class="title-text" transform="translate(40,30) rotate(31.66)" x="14" y="16"
          textLength="670" lengthAdjust="spacingAndGlyphs">SINGAPORE NATIONAL DAY PARTY</text>

    <polygon class="corner-sheet" points="430,1200 800,900 800,980 540,1200" fill="var(--paper)"/>

    <rect class="crowd" x="0" y="840" width="800" height="360" fill="url(#crowd-fill)"
          role="img" aria-label="Silhouettes of a diverse crowd dancing and celebrating"/>
  </svg>

  <section class="motto" aria-label="Many Voices, Shared Path, Tollvane Forever">
    <div class="motto-tab motto-tab--first">
      <div class="motto-badge"><span class="motto-ring">Many</span></div>
      <div class="motto-word">Voices</div>
    </div>
    <div class="motto-tab motto-tab--second">
      <div class="motto-badge"><span class="motto-ring">Shared</span></div>
      <div class="motto-word">Path</div>
    </div>
    <div class="motto-tab motto-tab--third">
      <div class="motto-badge"><span class="motto-ring">Tollvane</span></div>
      <div class="motto-word">Forever</div>
    </div>
  </section>
</main>
</body>
</html>
```